Business Cards & Letterhead etc.
Would like our Business Cards designed off our Logo
Professional
Dale Fenwick
PO Box 61309
Brenton, OR 97412
fenwickd@quellbridgeco.com
www.quellbridgeco.com
I would like the business cards to be designed so i can later alter the contact info for multiple people. Anything in Adobe is fine.

```html
<!DOCTYPE html>
<html lang="en">
<head>
<meta charset="utf-8">
<title>Quell IT Group – Business Cards</title>
<link href="https://fonts.googleapis.com/css2?family=Open+Sans:wght@400;600;700&display=swap" rel="stylesheet">
<style>
  :root {
    --page: #e9e6e2;
    --card-light: #ffffff;
    --card-dark: #0d0d0f;
    --blue: #1f8fe6;
    --blue-deep: #0a63c4;
    --blue-pale: #bfe0fb;
    --ink: #4d5056;
    --ink-soft: #6b6f76;
    --silver: #c9ccd1;
    --silver-soft: #9a9ea5;
  }
  * { margin: 0; padding: 0; box-sizing: border-box; }
  html, body { width: 1200px; height: 938px; overflow: hidden; }
  body {
    background: var(--page);
    font-family: "Open Sans", Arial, sans-serif;
    display: flex;
    flex-direction: column;
    align-items: center;
    justify-content: center;
    gap: 30px;
  }
  .card {
    position: relative;
    width: 740px;
    height: 423px;
    overflow: hidden;
    box-shadow: 0 6px 18px rgba(0,0,0,.18);
  }
  .card--front { background: var(--card-light); color: var(--ink); }
  .card--back { background: var(--card-dark); color: var(--silver); }

  .brand {
    position: absolute;
    left: 215px;
    top: 100px;
    display: flex;
    align-items: center;
    gap: 18px;
  }
  .brand__dot {
    width: 86px; height: 86px; border-radius: 50%;
    background: var(--blue);
  }
  .brand__name {
    font-weight: 700;
    font-size: 44px;
    line-height: 1;
    letter-spacing: 2px;
    text-transform: uppercase;
  }
  .brand__name span { display: block; font-size: 30px; letter-spacing: 3px; margin-top: 4px; }
  .card--front .brand__name { color: var(--ink); }
  .card--back .brand__name { color: var(--silver); }

  .name-band {
    position: absolute;
    left: 250px;
    top: 205px;
    width: 370px;
    height: 34px;
    background: linear-gradient(90deg, var(--blue-deep), var(--blue) 60%, #5ab8f5);
    color: #fff;
    font-size: 17px;
    font-weight: 600;
    display: flex;
    align-items: center;
    padding-left: 80px;
  }
  .name-band__rule { margin: 0 8px; font-weight: 400; }
  .band-square {
    position: absolute;
    left: 630px; top: 207px;
    width: 30px; height: 30px;
    background: var(--blue);
  }

  .contact-strip {
    position: absolute;
    left: 0; top: 262px;
    width: 740px; height: 24px;
    background: linear-gradient(90deg, var(--blue-pale), rgba(191,224,251,.5) 55%, rgba(191,224,251,0));
    display: flex;
    align-items: center;
    gap: 14px;
    padding-left: 22px;
    font-size: 11.5px;
    color: var(--ink-soft);
  }
  .card--back .contact-strip {
    background: linear-gradient(90deg, rgba(31,143,230,.45), rgba(31,143,230,.2) 55%, rgba(31,143,230,0));
    color: var(--silver-soft);
  }
  .contact-item { display: flex; align-items: center; gap: 4px; white-space: nowrap; }
  .contact-item svg { width: 9px; height: 9px; fill: var(--blue); }
  .address {
    position: absolute;
    left: 300px; top: 294px;
    font-size: 12px;
    color: var(--ink-soft);
  }
  .card--back .address { color: var(--silver-soft); }
</style>
</head>
<body>

<section class="card card--front">
  <div class="brand">
    <div class="brand__dot"></div>
    <div class="brand__name">Quell<span>IT Group</span></div>
  </div>
  <div class="name-band">Dale Fenwick<span class="name-band__rule">|</span>Owner</div>
  <div class="band-square"></div>
  <div class="contact-strip">
    <span class="contact-item"><svg viewBox="0 0 10 10"><rect x="2" y="0" width="6" height="10" rx="1"/></svg>555-201-0142</span>
    <span class="contact-item"><svg viewBox="0 0 10 10"><circle cx="5" cy="5" r="4"/></svg>555-202-0187</span>
    <span class="contact-item"><svg viewBox="0 0 10 10"><path d="M0 10 L5 1 L10 10Z"/></svg>555-203-0163</span>
    <span class="contact-item"><svg viewBox="0 0 10 10"><rect x="0" y="2" width="10" height="7"/></svg>fenwickd@quellbridgeco.com</span>
    <span class="contact-item"><svg viewBox="0 0 10 10"><circle cx="5" cy="5" r="4"/></svg>www.quellbridgeco.com</span>
  </div>
  <div class="address">PO Box 61309 Brenton, OR 97412</div>
</section>

<section class="card card--back">
  <div class="brand">
    <div class="brand__dot"></div>
    <div class="brand__name">Quell<span>IT Group</span></div>
  </div>
  <div class="name-band">Dale Fenwick<span class="name-band__rule">|</span>Owner</div>
  <div class="band-square"></div>
  <div class="contact-strip">
    <span class="contact-item"><svg viewBox="0 0 10 10"><rect x="2" y="0" width="6" height="10" rx="1"/></svg>555-201-0142</span>
    <span class="contact-item"><svg viewBox="0 0 10 10"><circle cx="5" cy="5" r="4"/></svg>555-202-0187</span>
    <span class="contact-item"><svg viewBox="0 0 10 10"><path d="M0 10 L5 1 L10 10Z"/></svg>555-203-0163</span>
    <span class="contact-item"><svg viewBox="0 0 10 10"><rect x="0" y="2" width="10" height="7"/></svg>fenwickd@quellbridgeco.com</span>
    <span class="contact-item"><svg viewBox="0 0 10 10"><circle cx="5" cy="5" r="4"/></svg>www.quellbridgeco.com</span>
  </div>
  <div class="address">PO Box 61309 Brenton, OR 97412</div>
</section>

</body>
</html>
```